Company Real Estate Site Needs A Face Lift

I need a new website for the recent company I formed: Tavenrow Real Estate.
You can use my agent website WWW.PALTUNE.COM to see the style/brand I already have. I will have areas for Searching for homes on QRV, etc.
I really like this site:
http://www.amberfieldhomestead.example/
I have attached my logo as well

Industry/Entity Type

Real Estate

Colors
0255a3
ffffff
cee9f5

```html
<!DOCTYPE html>
<html lang="en">
<head>
<meta charset="utf-8">
<title>Tavenrow Real Estate</title>
<link href="https://fonts.googleapis.com/css2?family=Lato:wght@400;700;900&display=swap" rel="stylesheet">
<style>
:root{
  --brand-blue:#0255a3;
  --bright-blue:#1a8fd6;
  --ice:#cee9f5;
  --white:#ffffff;
  --panel-dark:#232323;
  --footer-dark:#262626;
  --text-dark:#333333;
  --field-border:#a9a9a9;
  --progress-red:#c40000;
}
*{box-sizing:border-box;margin:0;padding:0}
html,body{width:1200px;height:778px;overflow:hidden}
body{position:relative;font-family:'Lato',sans-serif;background:var(--panel-dark)}
.hero-photo{position:absolute;left:0;top:0;width:1200px;height:731px;
  background:linear-gradient(180deg,#6fa8d8 0%,#b9d3e6 18%,#e7e8e3 40%,#d8d8d2 62%,#b5b7ad 78%,#c9ccc6 100%)}
.side-panel{position:absolute;left:0;top:0;width:420px;height:778px}
.brand{position:absolute;left:136px;top:34px;width:225px;text-align:center;color:var(--white);font-weight:900}
.brand-dot{width:24px;height:24px;border-radius:50%;background:var(--bright-blue);margin:0 auto 10px}
.brand-name{font-size:38px;letter-spacing:1px;line-height:1}
.brand-sub{font-size:19px;letter-spacing:5px;margin-top:8px;line-height:1}
.main-nav{position:absolute;left:136px;top:167px;width:225px;list-style:none}
.main-nav li{height:42px;line-height:42px;text-align:center;padding-right:28px;color:var(--white);font-weight:700;font-size:14px;
  border-bottom:1px solid #3a3a3a;background:linear-gradient(180deg,#2b2b2b,#1e1e1e)}
.main-nav li.active{background:linear-gradient(90deg,rgba(2,85,163,0) 0%,var(--brand-blue) 40%,#0a4d8f 70%,rgba(2,85,163,0) 100%)}
.search-card{position:absolute;left:327px;top:535px;width:468px;height:166px;background:#f2f2f2;border:4px solid #dcdcdc}
.search-head{height:37px;background:linear-gradient(180deg,#1a96dd,var(--brand-blue));color:var(--white);
  font-size:19px;display:flex;align-items:center;padding-left:14px;gap:10px}
.field-label{position:absolute;font-size:14px;color:var(--text-dark)}
.field{position:absolute;width:94px;height:21px;border:1px solid var(--field-border);background:var(--white);
  font-size:12px;color:#444;padding-left:6px;line-height:19px}
.field.select::after{content:"";position:absolute;right:0;top:0;width:19px;height:19px;background:#9a9a9a}
.field.select::before{content:"";position:absolute;right:5px;top:7px;border:5px solid transparent;border-top-color:#fff;z-index:1}
.adv-link{position:absolute;left:377px;top:75px;font-size:12px;color:var(--brand-blue);text-decoration:underline;line-height:17px}
.search-btn{position:absolute;left:375px;top:115px;width:71px;height:27px;background:linear-gradient(180deg,#1a96dd,var(--brand-blue));
  color:var(--white);font-weight:700;font-size:14px;text-align:center;line-height:27px;letter-spacing:.5px}
.video-card{position:absolute;left:806px;top:535px;width:263px;height:166px;border:4px solid #dcdcdc;background:#000}
.video-still{position:absolute;inset:0 0 26px 0;background:linear-gradient(180deg,#4f8fd0 0%,#9cc3e6 35%,#c9b98a 60%,#4f7a34 100%)}
.video-bar{position:absolute;left:0;right:0;bottom:0;height:26px;background:#111}
.site-footer{position:absolute;left:0;top:731px;width:1200px;height:47px;background:var(--footer-dark)}
.copyright{position:absolute;left:247px;top:16px;font-size:14px;color:#e8e8e8}
.social{position:absolute;top:10px;width:26px;height:26px;border-radius:50%;background:#f1f1f1}
</style>
</head>
<body>
<div class="hero-photo" role="img" aria-label="Photo of a modern two-storey white home with balcony, pool and garden"></div>

<svg class="side-panel" viewBox="0 0 420 778" aria-hidden="true">
  <path d="M0 0 H333 L398 131 L230 778 H0 Z" fill="#232323"/>
  <path d="M333 0 L398 131 L230 778" fill="none" stroke="#0255a3" stroke-width="6"/>
  <path d="M340 0 L404 131 L236 778" fill="none" stroke="#1a8fd6" stroke-width="1.5"/>
</svg>

<div class="brand">
  <div class="brand-dot"></div>
  <div class="brand-name">TAVENROW</div>
  <div class="brand-sub">REAL ESTATE</div>
</div>

<ul class="main-nav">
  <li class="active">HOME</li>
  <li>COMPANY</li>
  <li>BUY</li>
  <li>SELL</li>
  <li>TESTIMONIALS</li>
  <li>BLOG</li>
  <li>RESOURCES</li>
  <li>CONTACT</li>
</ul>

<section class="search-card">
  <div class="search-head">
    <svg width="24" height="24" viewBox="0 0 24 24" aria-hidden="true"><circle cx="10" cy="10" r="7" fill="none" stroke="#fff" stroke-width="3"/><path d="M15 15 L22 22" stroke="#fff" stroke-width="4" stroke-linecap="round"/></svg>
    Property Search
  </div>
  <span class="field-label" style="left:16px;top:56px">Location</span>
  <div class="field select" style="left:85px;top:55px">Select City</div>
  <span class="field-label" style="left:16px;top:89px">Max Price</span>
  <div class="field" style="left:85px;top:88px">500000</div>
  <span class="field-label" style="left:16px;top:122px">Min Beds</span>
  <div class="field" style="left:85px;top:121px">2</div>
  <span class="field-label" style="left:196px;top:56px">Min SQFT</span>
  <div class="field" style="left:263px;top:55px">0</div>
  <span class="field-label" style="left:196px;top:89px">Min Price</span>
  <div class="field" style="left:263px;top:88px">100000</div>
  <span class="field-label" style="left:196px;top:122px">Min Baths</span>
  <div class="field" style="left:263px;top:121px">1</div>
  <span class="adv-link">Advanced<br>Search</span>
  <div class="search-btn">SEARCH</div>
</section>

<section class="video-card">
  <div class="video-still" role="img" aria-label="Video still of a large suburban family house with lawn"></div>
  <svg style="position:absolute;left:104px;top:45px" width="52" height="52" viewBox="0 0 52 52" aria-hidden="true">
    <circle cx="26" cy="26" r="23" fill="rgba(255,255,255,.25)" stroke="#fff" stroke-width="2"/>
    <path d="M21 15 L36 26 L21 37 Z" fill="#fff"/>
  </svg>
  <div class="video-bar">
    <svg width="255" height="26" viewBox="0 0 255 26" aria-hidden="true">
      <path d="M8 8 L15 13 L8 18 Z" fill="#fff"/>
      <rect x="25" y="8" width="3" height="10" fill="#fff"/><rect x="31" y="8" width="3" height="10" fill="#fff"/>
      <rect x="49" y="11" width="161" height="5" fill="#777"/>
      <rect x="49" y="11" width="61" height="5" fill="#c40000"/>
      <path d="M230 12 V8 H234 M238 8 H242 V12 M242 16 V20 H238 M234 20 H230 V16" fill="none" stroke="#fff" stroke-width="2"/>
    </svg>
  </div>
</section>

<footer class="site-footer">
  <span class="copyright">Copyright © 2014 Tavenrow Real Estate.</span>
  <span class="social" style="left:939px" aria-label="Social link 1"></span>
  <span class="social" style="left:972px" aria-label="Social link 2"></span>
  <span class="social" style="left:1006px" aria-label="Social link 3"></span>
  <span class="social" style="left:1041px" aria-label="Social link 4"></span>
</footer>
</body>
</html>
```